Bold Website Design for Fitness Trainer - No Coding

We are in need of a bold and unique website design for a personal fitness training company, www.TessaLorvel.com. We need DESIGN ONLY for three pages. These will be a homepage, a lead capture page, and one internal page with a sidebar. The design will be used for coding a wordpress theme, if that matters for the designer.

Tessa Lorvel Fitness Training
2738 E 19th St #415
Austin, TX 78705
512-607-4918
http://www.tessalorvel.com

Target Market(s)

18-45 year old male and females making 80k+ a year and looking to get stronger and in shape.

Industry/Entity Type

Fitness

Number of Pages Required

3 page

Font styles to use
Sans Serif

Requirements
Must have
• See attached design specs file.
Nice to have
Should not have
• Boxed layout.
• Dark Background.

```html
<!DOCTYPE html>
<html lang="en">
<head>
<meta charset="utf-8">
<title>Tessa Lorvel Fitness Training – Homepage</title>
<link rel="stylesheet" href="https://fonts.googleapis.com/css2?family=Arimo:wght@400;700&family=Open+Sans:wght@400;600;700&display=swap">
<style>
:root{
  --stage:#000;
  --blue:#16ade8;
  --blue-text:#1a9ee0;
  --pink:#dc3f8d;
  --pink-line:#e0438c;
  --yellow:#e6d31c;
  --white:#fff;
  --page-bg:#f8f8f8;
  --grey-text:#8a8a8a;
  --nav-text:#8c8c8c;
  --field:#eeeeee;
  --card-img:#9e9e9e;
  --footer:#3a3a3a;
  --footer-bottom:#2e2e2e;
  --footer-text:#b9b9b9;
}
*{box-sizing:border-box;margin:0;padding:0}
html,body{width:1200px;height:1000px;overflow:hidden;background:var(--stage)}
body{position:relative;font-family:"Open Sans",Arial,sans-serif}
.frame{position:absolute;overflow:hidden;background:var(--page-bg)}
.frame--full{left:17px;top:45px;width:447px;height:915px}
.frame--full .page{transform:scale(.6296);transform-origin:0 0}
.frame--detail{left:473px;top:66px;width:710px;height:874px}
.page{position:relative;width:710px;height:1452px;background:var(--page-bg)}

/* top bar */
.topbar{height:30px;background:var(--blue);display:flex;align-items:center;padding:0 0 0 77px;color:var(--white);font-size:10px;font-weight:600}
.topbar__item{display:flex;align-items:center;gap:5px;margin-right:27px}
.topbar__item svg{display:block}
.topbar__social{margin-left:auto;display:flex;gap:4px;height:30px;align-items:center;border-left:1px solid rgba(255,255,255,.5);padding:0 80px 0 13px}
.dot{width:13px;height:13px;border:1px solid var(--white);border-radius:50%}

/* nav */
.mainnav{height:46px;background:var(--white);display:flex;align-items:center;padding-left:75px;box-shadow:0 1px 3px rgba(0,0,0,.15);position:relative;z-index:1}
.brand{display:flex;align-items:center;gap:6px;width:215px}
.brand__mark{width:30px;height:30px;border-radius:50%;background:var(--yellow)}
.brand__name{font-family:Arimo,Arial,sans-serif;font-weight:700;font-size:15px;color:#2b2b2b;line-height:1}
.menu{display:flex;list-style:none;font-family:Arimo,Arial,sans-serif;font-weight:700;font-size:9.5px;color:var(--nav-text)}
.menu li{margin-right:38px}
.menu .is-active{color:var(--blue)}

/* hero */
.hero{position:relative;height:251px;background:radial-gradient(circle at 62% 35%,#d8d8d8 0,#a7a7a7 35%,#6e6e6e 75%,#555 100%)}
.hero__offer{position:absolute;left:77px;top:107px;width:235px;height:75px;border:3px solid var(--pink-line);border-radius:7px;text-align:center;color:var(--pink-line);font-family:Arimo,Arial,sans-serif;font-weight:700;line-height:1.1}
.hero__offer span{display:block;font-size:21px;margin-top:5px}
.hero__offer strong{display:block;font-size:27px}
.hero__claim{position:absolute;left:77px;top:192px;font-family:Arimo,Arial,sans-serif;font-weight:700;font-size:23px;color:var(--yellow)}

/* cta bands */
.cta{text-align:center;color:var(--white)}
.cta--pink{height:129px;background:var(--pink);padding-top:9px}
.cta--blue{height:98px;background:var(--blue);padding-top:8px}
.cta__tags{font-family:Arimo,Arial,sans-serif;font-weight:700;font-size:13px;color:var(--yellow)}
.cta__title{font-family:Arimo,Arial,sans-serif;font-weight:700;font-size:38px;line-height:1;margin-top:10px}
.cta--blue .cta__title{margin-top:0}
.lead-form{display:flex;justify-content:center;gap:10px;margin-top:14px}
.lead-form span{width:130px;height:27px;background:var(--field);color:#9a9a9a;font-size:9px;text-align:left;padding:8px 9px;border:1px solid #ddd}
.lead-form b{width:76px;height:27px;background:var(--blue);color:var(--white);font-family:Arimo,Arial,sans-serif;font-size:13px;line-height:27px}
.cta--blue .lead-form{margin-top:10px}
.cta--blue .lead-form b{background:var(--pink)}

/* sections */
.section-title{font-family:Arimo,Arial,sans-serif;font-weight:700;font-size:23px;color:var(--blue-text);line-height:1}
.services{height:233px;padding:25px 78px 0 77px}
.services__intro{margin-top:12px;font-size:7.6px;line-height:2;color:var(--grey-text)}
.svc{display:flex;justify-content:center;margin-top:12px}
.svc__item{width:123px;text-align:center}
.svc__icon{width:44px;height:44px;margin:0 auto;border:1.5px solid #999;border-radius:50%;display:flex;align-items:center;justify-content:center}
.svc__arrow{width:5px;color:var(--blue);font-size:9px;margin-top:12px;text-align:center}
.svc__name{font-family:Arimo,Arial,sans-serif;font-weight:700;font-size:9px;color:var(--blue-text);margin-top:10px}
.svc__text{font-size:6.6px;line-height:1.7;color:#777;margin-top:4px}
.btn-small{display:inline-block;margin-top:9px;background:var(--blue);color:var(--white);font-size:4.5px;font-weight:700;padding:2px 5px}

.testimonials{height:181px;padding:5px 77px 0}
.cards{display:flex;gap:10px;margin-top:12px}
.card{width:132px;height:133px;background:var(--white);border:1px solid #e3e3e3;overflow:hidden}
.card__photo{height:76px;background:var(--card-img)}
.card__name{font-family:Arimo,Arial,sans-serif;font-weight:700;font-size:7px;color:#555;text-align:center;margin-top:5px}
.card__text{font-size:5.4px;line-height:1.55;color:#999;padding:5px 9px 0}

.blog{height:249px;padding:5px 77px 0}
.posts{margin-top:13px;list-style:none}
.post{display:flex;height:68px;align-items:flex-start}
.post__date{width:26px;height:26px;border:1.5px solid var(--blue);border-radius:50%;text-align:center;font-size:8px;font-weight:700;color:#555;line-height:1;padding-top:5px;margin-right:12px;flex:none}
.post__date small{display:block;font-size:4px;color:#999}
.post__body{width:220px}
.post__title{font-size:7.5px;font-weight:700;color:#444}
.post__meta{font-size:4.6px;color:#999;margin-top:2px}
.post__text{font-size:5.4px;line-height:1.6;color:#888;margin-top:5px}
.post__more{font-size:4.6px;color:#aaa;margin-top:4px}
.post__photo{margin-left:auto;width:96px;height:60px;background:linear-gradient(135deg,#4fb1de,#d67aa6 55%,#7aa9c8)}

/* footer */
.site-footer{height:191px;background:var(--footer);display:flex;padding:27px 0 0 78px;color:var(--footer-text);font-size:5.6px;line-height:1.6}
.fcol{width:138px}
.fcol:last-child{width:110px;margin-left:18px}
.fcol h4{font-size:7px;color:var(--white);font-weight:700;margin-bottom:8px}
.fcol p{margin-bottom:6px}
.fcol ul{list-style:none}
.fline{display:flex;gap:5px;margin-bottom:8px}
.fline i{flex:none;width:7px;height:7px;background:var(--blue);margin-top:2px}
.fline i.bar{width:2px;background:var(--blue)}
.box{background:#4b4b4b;border:1px solid #555;height:14px;margin-bottom:5px}
.box--tall{height:55px}
.fbtn{display:inline-block;border:1px solid var(--blue);color:var(--white);padding:1px 9px;font-size:5px;border-radius:2px}
.bottombar{height:44px;background:var(--footer-bottom);display:flex;align-items:center;padding:0 85px 0 78px;color:var(--footer-text);font-size:5.8px}
.bottombar .social{margin-left:auto;display:flex;gap:4px}
.bottombar .dot{border-color:#bbb}
</style>
</head>
<body>

<div class="frame frame--full">
<div class="page">
  <header class="topbar">
    <span class="topbar__item"><svg width="10" height="10" viewBox="0 0 10 10"><path d="M2 1l2 2-1 1.5c.6 1.2 1.3 1.9 2.5 2.5L7 6l2 2-1.5 1.5C4.5 9 1 5.5.5 2.5z" fill="#fff"/></svg>(555) 314 2087</span>
    <span class="topbar__item"><svg width="9" height="12" viewBox="0 0 9 12"><path d="M4.5 0A4.5 4.5 0 0 0 0 4.5C0 8 4.5 12 4.5 12S9 8 9 4.5A4.5 4.5 0 0 0 4.5 0zm0 6.3a1.8 1.8 0 1 1 0-3.6 1.8 1.8 0 0 1 0 3.6z" fill="#fff"/></svg>Locations</span>
    <span class="topbar__item"><svg width="13" height="13" viewBox="0 0 13 13"><rect x=".5" y="1.5" width="12" height="11" fill="none" stroke="#fff"/><rect x=".5" y="1.5" width="12" height="3" fill="#fff"/><path d="M3 7h2v2H3zm3 0h2v2H6zm3 0h2v2H9z" fill="#fff"/></svg>Appointment</span>
    <span class="topbar__social"><i class="dot"></i><i class="dot"></i><i class="dot"></i><i class="dot"></i><i class="dot"></i></span>
  </header>
  <nav class="mainnav">
    <div class="brand"><i class="brand__mark"></i><span class="brand__name">Tessa Lorvel</span></div>
    <ul class="menu"><li class="is-active">HOME</li><li>PAGES</li><li>JOURNAL</li><li>FEATURES</li><li>CONTACT</li></ul>
  </nav>
  <section class="hero" role="img" aria-label="Black and white photo of a woman stretching in a group fitness class">
    <div class="hero__offer"><span>Your First Session is</span><strong>FREE</strong></div>
    <p class="hero__claim">Austin's #1 Personal Trainer</p>
  </section>
  <section class="cta cta--pink">
    <p class="cta__tags">General Fitness • Weight Loss • Strength Training • Powerlifting</p>
    <h2 class="cta__title">GET STARTED TODAY</h2>
    <div class="lead-form"><span>Name</span><span>Email</span><span>Phone</span><b>SUBMIT</b></div>
  </section>
  <section class="services">
    <h2 class="section-title">SERVICES</h2>
    <p class="services__intro">Morbi leo risus, porta ac consectetur ac, vestibulum at eros. Cras mattis consectetur purus sit amet fermentum. Etiam porta sem malesuada magna mollis euismod. Nullam id dolor id nibh ultricies vehicula ut id elit. Aenean lacinia bibendum nulla sed consectetur posuere.</p>
    <div class="svc">
      <div class="svc__item"><div class="svc__icon"><svg width="24" height="24" viewBox="0 0 24 24"><path d="M4 3h16v2l-2 2H6L4 5zM7 8h10l-2 13H9z" fill="var(--blue)"/></svg></div><p class="svc__name">1-on-1 Personal Training</p><p class="svc__text">Vestibulum id ligula porta felis<br>euismod semper porta.</p><span class="btn-small">Read More</span></div>
      <div class="svc__arrow">›</div>
      <div class="svc__item"><div class="svc__icon"><svg width="24" height="22" viewBox="0 0 24 22"><rect x="2" y="2" width="20" height="13" rx="1" fill="none" stroke="var(--blue)" stroke-width="2"/><path d="M9 19h6M12 15v4" stroke="var(--blue)" stroke-width="2"/></svg></div><p class="svc__name">Online Coaching</p><p class="svc__text">Aenean eu leo quam ornare<br>sem lacinia qu venenatis</p><span class="btn-small">Read More</span></div>
      <div class="svc__arrow">›</div>
      <div class="svc__item"><div class="svc__icon"><svg width="26" height="14" viewBox="0 0 26 14"><path d="M1 4h3v6H1zM4 1h4v12H4zM8 6h10v2H8zM18 1h4v12h-4zM22 4h3v6h-3z" fill="var(--blue)"/></svg></div><p class="svc__name">Strength Programming</p><p class="svc__text">Praesent magnale scelerisque<br>nisl consectetur e nulla vitae.</p><span class="btn-small">Read More</span></div>
    </div>
  </section>
  <section class="testimonials">
    <h2 class="section-title">TESTIMONIALS</h2>
    <div class="cards">
      <div class="card"><div class="card__photo" role="img" aria-label="Client photo"></div><p class="card__name">John Doe</p><p class="card__text">Etiam porta sem malesuada magna mollis euismod. Sed posuere consectetur est at lobortis. Maecenas sed diam eget risus varius blandit sit amet non magna. Aenean lacinia bibendum nulla sed consectetur.</p></div>
      <div class="card"><div class="card__photo" role="img" aria-label="Client photo"></div><p class="card__name">John Doe</p><p class="card__text">Etiam porta sem malesuada magna mollis euismod. Sed posuere consectetur est at lobortis. Maecenas sed diam eget risus varius blandit sit amet non magna. Aenean lacinia bibendum nulla sed consectetur.</p></div>
      <div class="card"><div class="card__photo" role="img" aria-label="Client photo"></div><p class="card__name">John Doe</p><p class="card__text">Etiam porta sem malesuada magna mollis euismod. Sed posuere consectetur est at lobortis. Maecenas sed diam eget risus varius blandit sit amet non magna. Aenean lacinia bibendum nulla sed consectetur.</p></div>
      <div class="card"><div class="card__photo" role="img" aria-label="Client photo"></div><p class="card__name">John Doe</p><p class="card__text">Etiam porta sem malesuada magna mollis euismod. Sed posuere consectetur est at lobortis. Maecenas sed diam eget risus varius blandit sit amet non magna. Aenean lacinia bibendum nulla sed consectetur.</p></div>
    </div>
  </section>
  <section class="blog">
    <h2 class="section-title">LATEST BLOG POSTS</h2>
    <ul class="posts">
      <li class="post"><div class="post__date">23<small>JUN</small></div><div class="post__body"><p class="post__title">Aenean Adipiscing Etiam Vestibulum</p><p class="post__meta">Productivity | 8 Comments | 17</p><p class="post__text">Etiam porta sem malesuada magna mollis euismod. Aenean leo quam. Pellentesque ornare sem lacinia quam venenatis vestibulum.</p><p class="post__more">Continue Reading →</p></div><div class="post__photo" role="img" aria-label="Photo of a group stretching class"></div></li>
      <li class="post"><div class="post__date">21<small>JUN</small></div><div class="post__body"><p class="post__title">Commodo Sem Inceptos Fusce</p><p class="post__meta">Heart Healthy | 5 Comments | 12</p><p class="post__text">Duis mollis, est non commodo luctus, nisi erat porttitor ligula, eget lacinia odio sem nec elit. Cras mattis purus.</p><p class="post__more">Continue Reading →</p></div><div class="post__photo" role="img" aria-label="Photo of a spin class in a gym"></div></li>
      <li class="post"><div class="post__date">21<small>JUN</small></div><div class="post__body"><p class="post__title">Commodo Sem Inceptos Fusce</p><p class="post__meta">Strength Training | 11 Comments | 9</p><p class="post__text">Duis mollis, est non commodo luctus, nisi erat porttitor ligula, eget lacinia odio sem nec elit. Cras mattis purus.</p><p class="post__more">Continue Reading →</p></div><div class="post__photo" role="img" aria-label="Photo of people stretching on mats"></div></li>
    </ul>
  </section>
  <section class="cta cta--blue">
    <h2 class="cta__title">GET STARTED TODAY</h2>
    <div class="lead-form"><span>Name</span><span>Email</span><span>Phone</span><b>SUBMIT</b></div>
  </section>
  <footer class="site-footer">
    <div class="fcol"><h4>Get In Touch</h4><p>Fusce dapibus, tellus commodo, tortor mauris condimentum utellus fermentum, porta sem malesuada magna.</p><div class="fline"><i></i><span>Harbor Lane No 22/18<br>Austin, TEXAS</span></div><div class="fline"><i></i><span>0148 377 26 09</span></div><div class="fline"><i></i><span>support@tessalorvel.com</span></div><h4>Resources</h4><ul><li>• Link1</li><li>• Link2</li><li>• Link3</li></ul></div>
    <div class="fcol"><h4>Photo Feed</h4><div class="fline"><i></i><span>Aenean lacinia bibendum nulla sed eu posuere erat a ante venenatis dapibus posuere velit aliquet.</span></div><div class="fline"><i></i><span>Donec ullamcorper metus auctor fringilla. Nullam quis risus eget.</span></div><div class="fline"><i></i><span>Vestibulum id ligula porta euismod semper. Maecenas faucibus mollis.</span></div></div>
    <div class="fcol"><h4>Latest News</h4><div class="fline"><i class="bar"></i><span>Vivamus sagittis lacus vel augue laoreet rutrum dolor auctor.<br>14 Nov, 2013</span></div><div class="fline"><i class="bar"></i><span>Scelerisque nisi consectetur et.<br>02 May, 2013</span></div><div class="fline"><i class="bar"></i><span>Pellentesque ornare sem lacinia quam venenatis vestibulum. Fusce<br>15 July, 2013</span></div></div>
    <div class="fcol"><h4>Contact Form</h4><div class="box"></div><div class="box"></div><div class="box box--tall"></div><span class="fbtn">Submit</span></div>
  </footer>
  <div class="bottombar"><span>© 2015 Tessa Lorvel. All Rights Reserved.</span><span class="social"><i class="dot"></i><i class="dot"></i><i class="dot"></i><i class="dot"></i><i class="dot"></i></span></div>
</div>
</div>

<div class="frame frame--detail">
<div class="page">
  <header class="topbar">
    <span class="topbar__item"><svg width="10" height="10" viewBox="0 0 10 10"><path d="M2 1l2 2-1 1.5c.6 1.2 1.3 1.9 2.5 2.5L7 6l2 2-1.5 1.5C4.5 9 1 5.5.5 2.5z" fill="#fff"/></svg>(555) 314 2087</span>
    <span class="topbar__item"><svg width="9" height="12" viewBox="0 0 9 12"><path d="M4.5 0A4.5 4.5 0 0 0 0 4.5C0 8 4.5 12 4.5 12S9 8 9 4.5A4.5 4.5 0 0 0 4.5 0zm0 6.3a1.8 1.8 0 1 1 0-3.6 1.8 1.8 0 0 1 0 3.6z" fill="#fff"/></svg>Locations</span>
    <span class="topbar__item"><svg width="13" height="13" viewBox="0 0 13 13"><rect x=".5" y="1.5" width="12" height="11" fill="none" stroke="#fff"/><rect x=".5" y="1.5" width="12" height="3" fill="#fff"/><path d="M3 7h2v2H3zm3 0h2v2H6zm3 0h2v2H9z" fill="#fff"/></svg>Appointment</span>
    <span class="topbar__social"><i class="dot"></i><i class="dot"></i><i class="dot"></i><i class="dot"></i><i class="dot"></i></span>
  </header>
  <nav class="mainnav">
    <div class="brand"><i class="brand__mark"></i><span class="brand__name">Tessa Lorvel</span></div>
    <ul class="menu"><li class="is-active">HOME</li><li>PAGES</li><li>JOURNAL</li><li>FEATURES</li><li>CONTACT</li></ul>
  </nav>
  <section class="hero" role="img" aria-label="Black and white photo of a woman stretching in a group fitness class">
    <div class="hero__offer"><span>Your First Session is</span><strong>FREE</strong></div>
    <p class="hero__claim">Austin's #1 Personal Trainer</p>
  </section>
  <section class="cta cta--pink">
    <p class="cta__tags">General Fitness • Weight Loss • Strength Training • Powerlifting</p>
    <h2 class="cta__title">GET STARTED TODAY</h2>
    <div class="lead-form"><span>Name</span><span>Email</span><span>Phone</span><b>SUBMIT</b></div>
  </section>
  <section class="services">
    <h2 class="section-title">SERVICES</h2>
    <p class="services__intro">Morbi leo risus, porta ac consectetur ac, vestibulum at eros. Cras mattis consectetur purus sit amet fermentum. Etiam porta sem malesuada magna mollis euismod. Nullam id dolor id nibh ultricies vehicula ut id elit. Aenean lacinia bibendum nulla sed consectetur posuere.</p>
    <div class="svc">
      <div class="svc__item"><div class="svc__icon"><svg width="24" height="24" viewBox="0 0 24 24"><path d="M4 3h16v2l-2 2H6L4 5zM7 8h10l-2 13H9z" fill="var(--blue)"/></svg></div><p class="svc__name">1-on-1 Personal Training</p><p class="svc__text">Vestibulum id ligula porta felis<br>euismod semper porta.</p><span class="btn-small">Read More</span></div>
      <div class="svc__arrow">›</div>
      <div class="svc__item"><div class="svc__icon"><svg width="24" height="22" viewBox="0 0 24 22"><rect x="2" y="2" width="20" height="13" rx="1" fill="none" stroke="var(--blue)" stroke-width="2"/><path d="M9 19h6M12 15v4" stroke="var(--blue)" stroke-width="2"/></svg></div><p class="svc__name">Online Coaching</p><p class="svc__text">Aenean eu leo quam ornare<br>sem lacinia qu venenatis</p><span class="btn-small">Read More</span></div>
      <div class="svc__arrow">›</div>
      <div class="svc__item"><div class="svc__icon"><svg width="26" height="14" viewBox="0 0 26 14"><path d="M1 4h3v6H1zM4 1h4v12H4zM8 6h10v2H8zM18 1h4v12h-4zM22 4h3v6h-3z" fill="var(--blue)"/></svg></div><p class="svc__name">Strength Programming</p><p class="svc__text">Praesent magnale scelerisque<br>nisl consectetur e nulla vitae.</p><span class="btn-small">Read More</span></div>
    </div>
  </section>
  <section class="testimonials">
    <h2 class="section-title">TESTIMONIALS</h2>
    <div class="cards">
      <div class="card"><div class="card__photo" role="img" aria-label="Client photo"></div><p class="card__name">John Doe</p><p class="card__text">Etiam porta sem malesuada magna mollis euismod. Sed posuere consectetur est at lobortis. Maecenas sed diam eget risus varius blandit sit amet non magna. Aenean lacinia bibendum nulla sed consectetur.</p></div>
      <div class="card"><div class="card__photo" role="img" aria-label="Client photo"></div><p class="card__name">John Doe</p><p class="card__text">Etiam porta sem malesuada magna mollis euismod. Sed posuere consectetur est at lobortis. Maecenas sed diam eget risus varius blandit sit amet non magna. Aenean lacinia bibendum nulla sed consectetur.</p></div>
      <div class="card"><div class="card__photo" role="img" aria-label="Client photo"></div><p class="card__name">John Doe</p><p class="card__text">Etiam porta sem malesuada magna mollis euismod. Sed posuere consectetur est at lobortis. Maecenas sed diam eget risus varius blandit sit amet non magna. Aenean lacinia bibendum nulla sed consectetur.</p></div>
      <div class="card"><div class="card__photo" role="img" aria-label="Client photo"></div><p class="card__name">John Doe</p><p class="card__text">Etiam porta sem malesuada magna mollis euismod. Sed posuere consectetur est at lobortis. Maecenas sed diam eget risus varius blandit sit amet non magna. Aenean lacinia bibendum nulla sed consectetur.</p></div>
    </div>
  </section>
</div>
</div>

</body>
</html>
```